Specialist Medical practice after professional trifold flyer design for patient information brochure

I am the Director of the Hollowbrook Clinic, a specialist medial and surgical practice in Australia. I am after a professional design of a patient information trifold flyer that can be used for web distribution or for commercial printing for upcoming educational event. The design would need to allow change of images and text to be used as template for future topics but have a common brand look across them. Colours would follow the logo, but primarily blue colours for the hollowbrook theme. The inside text needs to be clearly contrasted to the background for easy reading, as often elderly patients. The design would make use of curves or circles, but open for hexagonal, triangle square vector components. I have included an outline for the initial brochure and included images to include. Other stock background images can be used if they increase the impact of the design over included. A winning design is also one that could be modified to a 4 page bi-fold brochure

Target Market(s)

This will be provided to patients in GP practices, podiatry clinics, radiological practices. Aimed at patients to read and be compelled to look to site or get consultation with me

Industry/Entity Type

Medical

Font styles to use
Serif
Sans Serif

Colors
33a6d7
0355a3
86cfc6
cedeed
0292cd
85cae6

Requirements
Must have
• The front cover needs to engage the patient to pick up and read- yes I have a painful ankle and want to find out more. the goal for the inside is to provide the options but be able to direct to website for more info - website currently undergoing upgrade. After professional modern look. Not bright contrasting colours like many advertising brochures. Needs to able to have images and text changed but following same look to create new topics
Nice to have
• The focus is a Tri-fold brochure. Nice to be able to modify to bifold. A winning design would even offer both, or submit separate bifold and trifold. I am open to different versions of similar look. (eg option of brochure with curved elements, triangular or square, or hexagonal.
Should not have
• To many contrasting colours. Text must be easily read on background, either white or coloured background texture with transparency

```html
<!DOCTYPE html>
<html lang="en">
<head>
<meta charset="utf-8">
<title>Hollowbrook Clinic – My Painful Ankle trifold</title>
<link href="https://fonts.googleapis.com/css2?family=Open+Sans:ital,wght@0,400;0,600;1,400;1,600&family=Fira+Sans:wght@500;600;700&display=swap" rel="stylesheet">
<style>
:root{
  --navy:#1d4c9c;
  --blue:#2b62b6;
  --blue-deep:#0355a3;
  --sky:#33a6d7;
  --sky-soft:#85cae6;
  --mist:#cedeed;
  --ribbon:#e3405a;
  --ink:#4a4f57;
  --white:#ffffff;
  --page:#e6e8ec;
}
*{box-sizing:border-box;margin:0;padding:0}
html,body{width:1200px;height:1200px;overflow:hidden;background:var(--page)}
body{position:relative;font-family:"Open Sans",sans-serif}
.spread{position:absolute;left:230px;width:740px;height:572px;display:flex;box-shadow:0 6px 18px rgba(0,0,0,.18);overflow:hidden}
.spread--inside{top:20px}
.spread--outside{top:608px}
.panel{position:relative;width:246.67px;height:100%;overflow:hidden}
.panel--white{background:var(--white);color:var(--ink)}
.panel--blue{background:linear-gradient(160deg,#2d66ba 0%,#2356a8 55%,#1d4c9c 100%);color:var(--white)}
.panel--blue + .panel--blue{border-left:1px solid rgba(255,255,255,.08)}
.copy{position:absolute;font-size:8.1px;line-height:1.38;font-style:italic;text-align:justify}
.copy p+p{margin-top:8px}
.photo{position:absolute}
.ribbon{position:absolute;background:var(--ribbon);color:var(--white);font-family:"Fira Sans",sans-serif;font-weight:600;font-size:10.5px;padding:3px 6px;border-radius:2px;box-shadow:0 2px 3px rgba(0,0,0,.25)}
.side-note{position:absolute;color:var(--white);font-size:8.8px;font-style:italic;line-height:1.4}
.url-pill{display:block;margin-top:4px;background:linear-gradient(#3aa8e0,#1f7fcb);border-radius:3px;padding:2px 5px;font-size:7.4px;line-height:1.15;font-style:normal;box-shadow:0 2px 3px rgba(0,0,0,.25)}
.curves{position:absolute;inset:0;width:100%;height:100%;pointer-events:none}
.brand{display:flex;align-items:center;gap:6px;font-family:"Fira Sans",sans-serif;font-weight:600;letter-spacing:.5px}
.brand__dot{width:14px;height:14px;border-radius:50%;background:currentColor;opacity:1}
.cover-title{position:absolute;font-family:"Fira Sans",sans-serif;font-weight:600;color:var(--white)}
.bio-name{position:absolute;left:22px;top:120px;color:var(--sky);font-style:italic;font-size:10.5px;line-height:1.05}
.bio-quals{font-size:6.6px;color:var(--ink);line-height:1.35;margin-top:3px;font-style:normal}
.conditions{position:absolute;left:22px;right:14px;top:412px;color:var(--white)}
.conditions h3{font-size:12px;font-weight:400;font-style:italic;margin-bottom:12px}
.conditions .lead{font-size:7.2px;font-style:italic;line-height:1.35;margin-bottom:10px}
.cond-item{font-size:7px;font-style:italic;line-height:1.4;color:var(--mist);padding-left:7px;border-left:2px solid var(--ribbon);margin-bottom:11px}
.cond-item--gold{border-color:#e8b33a}
.contact{position:absolute;left:18px;right:14px;top:410px;color:var(--white);font-size:8.6px}
.contact h3{font-family:"Fira Sans",sans-serif;font-weight:600;font-size:12.5px;margin-bottom:2px}
.contact .addr{font-size:7.4px;line-height:1.35}
.contact-row{display:flex;gap:10px;align-items:flex-start}
.contact-row svg{flex:none;margin-top:2px}
.rule{border-top:1px dashed rgba(255,255,255,.6);margin:5px 0 5px 24px}
.cover-meta{position:absolute;right:14px;text-align:right;color:var(--white);font-style:italic}
.cover-meta b{display:block;font-size:9px;font-weight:600}
.cover-meta span{display:block;font-size:6.4px;font-weight:600}
</style>
</head>
<body>

<!-- Inside spread -->
<section class="spread spread--inside">
  <div class="panel panel--white">
    <div class="photo" role="img" aria-label="Doctor in white coat holding an ankle x-ray" style="left:0;top:0;width:100%;height:155px;background:linear-gradient(180deg,#dfe6ee 0%,#f4f6f8 60%,#ffffff 100%)"></div>
    <div class="copy" style="left:22px;right:22px;top:168px">
      <p>Ankle arthritis is a painful condition where there is loss of cartilage from the ankle joint surface. Although not as common as knee or hip arthritis, pain can be debilitating affecting quality of life.</p>
      <p>Arthritis of the joint can be caused by trauma joint such as fracture or recurrent instability or secondary from inflammatory conditions such as rheumatoid arthritis.</p>
      <p>Pain from the joint will occur with activity causing a limp, limiting walking speed and distance. Often there is swelling of the joint with progressive loss of motion.</p>
      <p>Diagnosis is made with examination of the ankle and weight bearing x-rays showing loss of joint space.</p>
    </div>
    <div class="photo" role="img" aria-label="Side x-ray of an arthritic ankle" style="left:22px;top:378px;width:202px;height:160px;background:linear-gradient(135deg,#0c0c0c 0%,#5a5a5a 45%,#1a1a1a 75%,#111 100%)"></div>
  </div>

  <div class="panel panel--blue">
    <svg class="curves" viewBox="0 0 247 572" aria-hidden="true"><path d="M-20 420 C 80 520, 190 560, 260 520" fill="none" stroke="#3a78c9" stroke-width="34" opacity=".35"/></svg>
    <div class="copy" style="left:22px;right:22px;top:30px">
      <p>When pain medication, activity modification and shoe ware modification is no longer effective to control the pain then it is worthwhile discussing with your GP for referral to Dr Martin Halloway for an opinion on further treatment. As an Orthopaedic Foot and Ankle surgeon, he will be able to assess your conditions and give advice on the best options for your treatment.</p>
      <p>The decision on the best option is based on your age, activity level, existing medical problems, previous ankle treatment and your expected outcome from treatment. In the situation of end stage arthritis options consist of either Ankle fusion or Total Ankle replacement.</p>
    </div>
    <div class="ribbon" style="left:18px;top:224px">Ankle Fusion Surgery.</div>
    <div class="copy" style="left:22px;right:22px;top:256px">
      <p>This operation aims to stiffen the ankle joint by fusing the tibia and talus together in the optimal position for function. The common thought is that there will be no movement of the foot, and the patient will walk with a limp. The fusion only occurs at the ankle joint, leaving motion available to the surrounding joints. Although there is decreased motion, you will walk more normally after a fusion without a limp as the pain to the joint is removed.</p>
    </div>
    <div class="photo" role="img" aria-label="X-ray of ankle fusion with plate and screws" style="left:20px;top:380px;width:106px;height:147px;background:linear-gradient(150deg,#111 0%,#6f6f6f 40%,#2a2a2a 70%,#0d0d0d 100%)"></div>
    <div class="side-note" style="left:146px;top:383px;width:94px">For more information on ankle fusion, risks and recovery</div>
    <div class="side-note" style="left:146px;top:435px;width:94px">visit our website :<span class="url-pill">www.hollowbrookclinic.<br>com.au/Ankle-Fusion</span></div>
    <div class="side-note" style="left:146px;top:487px;width:94px">Total Ankle Replacement Surgery</div>
  </div>

  <div class="panel panel--blue">
    <svg class="curves" viewBox="0 0 247 572" aria-hidden="true"><path d="M150 0 C 300 120, 280 420, 120 572" fill="none" stroke="#3a78c9" stroke-width="40" opacity=".3"/></svg>
    <div class="copy" style="left:22px;right:22px;top:30px">
      <p>In suitable patients there may be the option to maintain joint motion and perform a Total Ankle Replacement. Like a hip or knee replacement operation, the arthritic joint is removed and replaced with an artificial joint. Like an ankle fusion there will alleviation of the pain and limp with maintenance of the ankle joint motion. Recovery to walking post-surgery is often much sooner than with ankle fusion. Dr Martin Halloway is one of the few surgeons to have completed an international fellowship in ankle replacement surgery and has been performing the technique since 2008. He is currently performing the technique using the Meridian total ankle with Contour guides.</p>
    </div>
    <div class="photo" role="img" aria-label="X-ray of total ankle replacement implant" style="left:22px;top:197px;width:92px;height:110px;background:linear-gradient(150deg,#0e0e0e 0%,#7a7a7a 40%,#262626 75%,#0d0d0d 100%)"></div>
    <div class="side-note" style="left:135px;top:206px;width:100px;font-size:8px">For more information on ankle fusion, risks and recovery</div>
    <div class="side-note" style="left:133px;top:246px;width:100px;font-size:8px">visit our website :<span class="url-pill" style="font-size:6.4px">www.hollowbrookclinic.com.au<br>/Ankle-Replacement</span></div>
    <div class="ribbon" style="left:14px;top:340px">Results of surgery</div>
    <div class="copy" style="left:22px;right:18px;top:370px;font-size:7.9px">
      <p>Successful surgery in the suitable patient will help resolve the pain associated with the ankle arthritis. Ankle Fusion surgery is ideal for patients with heavy labour work, allowing them to return to previous activities. There may be the risk of arthritis to surrounding joints in the future, but often this occurs many years down the track. Results from Total Ankle replacement surgery have been improving over the years, but there is known risks of loosening, cyst formation or failure of the joint over time that can occur in some patients. It is important to have a opinion from an Orthopaedic Foot and Ankle Surgeon experienced in the these procedure to determine which procedure will provide the best long term solution for you.</p>
    </div>
  </div>
</section>

<!-- Outside spread -->
<section class="spread spread--outside">
  <div class="panel panel--white">
    <div class="copy" style="left:22px;right:20px;top:24px;font-size:7.2px">
      <p>Dr Martin Halloway is an Australian trained Orthopaedic Surgeon who has a primary focus in the treatment of conditions of the foot and ankle. He has completed post fellowship training in Foot and Ankle surgery both locally and internationally, and continues to update himself in the latest techniques.</p>
    </div>
    <div class="bio-name">Dr Martin<br>Halloway
      <div class="bio-quals">MBBS (NCU),<br>FRACS (Ortho),<br>FA (Ortho)</div>
    </div>
    <div class="photo" role="img" aria-label="Portrait of the surgeon in a dark suit and blue tie" style="left:82px;top:88px;width:165px;height:300px;background:linear-gradient(180deg,#f2f3f5 0%,#e6d6cc 35%,#2b2f3a 70%,#1d2029 100%)"></div>
    <svg class="curves" viewBox="0 0 247 572" aria-hidden="true" preserveAspectRatio="none">
      <path d="M0 210 C 10 340, 120 390, 247 392 L247 572 L0 572 Z" fill="#2b5fb2"/>
      <path d="M0 210 C 8 300, 70 360, 247 380" fill="none" stroke="#33a6d7" stroke-width="6"/>
      <path d="M0 240 C 14 330, 90 372, 247 388" fill="none" stroke="#85cae6" stroke-width="3"/>
    </svg>
    <div class="conditions">
      <h3>Conditions treated</h3>
      <p class="lead">Dr Halloway provides assessment and treatment of all foot and ankle conditions. He has special interest in the following:</p>
      <p class="cond-item">Minimally invasive treatment for bunions and toe deformities. Joint sparing procedures for arthritis or deformity, including the Ventra implant.</p>
      <p class="cond-item">Joint fusion procedures for arthritis of the feet and ankle Sports injuries and tendinopathies.</p>
      <p class="cond-item cond-item--gold">Total ankle replacement and deformity correction of the foot and ankle.</p>
    </div>
  </div>

  <div class="panel panel--blue">
    <div class="photo" role="img" aria-label="Modern white hospital building against a blue sky" style="left:0;top:0;width:100%;height:300px;background:linear-gradient(180deg,#2f69b8 0%,#5d8fcc 45%,#a9c2dd 70%,#8e9a8c 100%)"></div>
    <div class="brand" style="position:absolute;left:22px;top:22px;color:var(--white);font-size:10px"><span class="brand__dot" style="width:10px;height:10px"></span>HOLLOWBROOK CLINIC</div>
    <div style="position:absolute;left:0;top:300px;width:100%;height:98px;background:linear-gradient(180deg,#ffffff 0%,#e8eef5 100%);display:flex;align-items:center;justify-content:center">
      <div class="brand" style="color:var(--blue-deep);font-size:15px"><span class="brand__dot"></span>HOLLOWBROOK CLINIC</div>
    </div>
    <div class="contact">
      <div class="contact-row">
        <svg width="10" height="12" viewBox="0 0 10 12"><path d="M5 0a4 4 0 0 0-4 4c0 3 4 8 4 8s4-5 4-8a4 4 0 0 0-4-4zm0 5.5A1.5 1.5 0 1 1 5 2.5a1.5 1.5 0 0 1 0 3z" fill="#fff"/></svg>
        <div><h3>Hollowbrook Clinic</h3><p class="addr">-Suite 701-701, Level 7, Kestrel Bay Private Hospital<br>360-364 Marine St Kestrel Bay NSW<br>-70 Mill Road Ashford NSW</p></div>
      </div>
      <div class="rule"></div>
      <div class="contact-row">
        <svg width="10" height="22" viewBox="0 0 10 22"><path d="M2 1l2 2-1 2c1 2 2 3 4 4l2-1 1 2-2 1C4 10 1 6 1 2z" fill="#fff"/><rect x="1" y="13" width="8" height="7" rx="1" fill="#fff"/></svg>
        <p style="line-height:1.25">(02) 5550 1870<br>(02) 5550 1502</p>
      </div>
      <div class="rule"></div>
      <div class="contact-row">
        <svg width="10" height="8" viewBox="0 0 10 8"><rect x=".5" y=".5" width="9" height="7" fill="none" stroke="#fff"/><path d="M.5 .5L5 4.5 9.5 .5" fill="none" stroke="#fff"/></svg>
        <p>info@hollowbrookclinic.com.au</p>
      </div>
      <div class="rule"></div>
      <div class="contact-row">
        <svg width="10" height="10" viewBox="0 0 10 10"><circle cx="5" cy="5" r="4.4" fill="none" stroke="#fff"/><path d="M.6 5h8.8M5 .6c-2.4 2.6-2.4 6.2 0 8.8M5 .6c2.4 2.6 2.4 6.2 0 8.8" fill="none" stroke="#fff" stroke-width=".8"/></svg>
        <p>www.hollowbrookclinic.com.au</p>
      </div>
    </div>
  </div>

  <div class="panel panel--blue">
    <div class="photo" role="img" aria-label="Runner holding a sore ankle on a sunny trail" style="left:0;top:0;width:100%;height:400px;background:linear-gradient(180deg,#8a6a4c 0%,#c99a6a 35%,#e8c48a 55%,#b89a62 80%,#7e6c45 100%)"></div>
    <svg class="curves" viewBox="0 0 247 572" aria-hidden="true" preserveAspectRatio="none">
      <path d="M0 572 L0 470 C 30 370, 130 340, 247 330 L247 572 Z" fill="#1f4fa0"/>
      <path d="M0 500 C 25 390, 120 350, 247 338" fill="none" stroke="#33a6d7" stroke-width="7"/>
      <path d="M8 520 C 40 410, 130 368, 247 352" fill="none" stroke="#85cae6" stroke-width="2.5" opacity=".8"/>
    </svg>
    <div class="cover-title" style="left:28px;top:260px;padding:4px 10px;background:var(--ribbon);border-radius:4px;font-size:18px;box-shadow:0 2px 4px rgba(0,0,0,.25)">my painful ankle</div>
    <div class="cover-title" style="left:66px;top:310px;width:166px;padding:4px 10px;background:var(--blue-deep);border-radius:4px;font-size:17px;line-height:1.1;text-align:right;box-shadow:0 2px 4px rgba(0,0,0,.25)">Solution for<br>ankle arthritis</div>
    <div class="brand" style="position:absolute;right:14px;top:436px;color:var(--white);font-size:12.5px"><span class="brand__dot" style="width:12px;height:12px"></span>HOLLOWBROOK CLINIC</div>
    <div class="cover-meta" style="top:493px"><b>My Painful Ankle</b><span>Solutions for Ankle Arthritis</span></div>
    <div class="cover-meta" style="top:527px"><b>Dr Martin Halloway</b><span>Orthopaedic Foot and Ankle Surgeon</span></div>
  </div>
</section>

</body>
</html>
```